Saffron Lotus Court Business Card

I am looking for a business card desgined for my restaurant. It is an Indian restaurant, we are looking for something thats modern, yet traditional with the indian culture, we are looking for colors that match our logo. The logo is a design of the building with the name of the restaurant. for more information on the restaurant go to www.saffronlotuscourt.example

Industry/Entity Type

Indian Restaurant

Contact Information for Business Card

we are looking for somthing thats modern, yet traditional with the indian culture, we are looking for colors that match our logo. The logo is a design of the building with the name of the restaurant. for more information on the restaurant go to www.saffronlotuscourt.example

Requirements
Must have
• The logo that is attached,
• Name: Harjot Banwal,
• address of the restaurant: 2917 West Tamarind Ave, Phoenix, Arizona, 85047
• Phone: (602) 517-3094
• Fax: (602) 768-2145
• Restaurant Catering Banquet
• Website: www.SaffronLotusCourt.example
Nice to have
• wanted to get something that goes with the theme of the restaurant, which is traditional but also keep a very professional and modern touch

```html
<!DOCTYPE html>
<html lang="en">
<head>
<meta charset="utf-8">
<title>Saffron Lotus Court Business Card</title>
<link href="https://fonts.googleapis.com/css2?family=Open+Sans:wght@400;600;700&display=swap" rel="stylesheet">
<style>
  :root {
    --backdrop: #4a413c;
    --card: #111010;
    --card-edge: #1c1a19;
    --saffron: #f07c1e;
    --brand-red: #e0512a;
    --text-light: #f2f2f2;
    --divider: #c4621c;
  }
  * { margin: 0; padding: 0; box-sizing: border-box; }
  html, body {
    width: 1200px;
    height: 900px;
    overflow: hidden;
  }
  body {
    background: var(--backdrop);
    font-family: "Open Sans", Arial, sans-serif;
    position: relative;
  }
  .card {
    position: absolute;
    top: 296px;
    width: 540px;
    height: 309px;
    background: var(--card);
    border: 1px solid var(--card-edge);
    box-shadow: 0 10px 24px rgba(0,0,0,0.45);
  }
  .card--contact { left: 40px; }
  .card--front { left: 620px; }

  .brand-name {
    color: var(--brand-red);
    font-weight: 600;
    text-transform: uppercase;
    text-align: center;
    line-height: 1.12;
    letter-spacing: 2px;
  }

  .contact-brand {
    position: absolute;
    left: 0;
    top: 0;
    width: 270px;
    height: 100%;
    display: flex;
    align-items: center;
    justify-content: center;
  }
  .contact-brand .brand-name { font-size: 30px; }

  .contact-divider {
    position: absolute;
    left: 276px;
    top: 52px;
    width: 1px;
    height: 200px;
    background: var(--divider);
  }

  .contact-details {
    position: absolute;
    left: 300px;
    top: 58px;
    color: var(--text-light);
    font-size: 13.5px;
    line-height: 1.45;
  }
  .person-name {
    color: var(--saffron);
    font-weight: 700;
    font-size: 17px;
    margin-bottom: 26px;
  }
  .address { margin-bottom: 16px; }
  .contact-list { list-style: none; }
  .contact-list li {
    display: flex;
    align-items: center;
    gap: 9px;
  }
  .contact-list svg { width: 11px; height: 11px; flex: none; }

  .card--front {
    display: flex;
    align-items: center;
    justify-content: center;
  }
  .card--front .brand-name { font-size: 40px; }
</style>
</head>
<body>

  <section class="card card--contact" aria-label="Business card, contact side">
    <div class="contact-brand">
      <p class="brand-name">Saffron<br>Lotus<br>Court</p>
    </div>
    <div class="contact-divider"></div>
    <div class="contact-details">
      <p class="person-name">Harjot Banwal</p>
      <p class="address">2917 West Tamarind Ave,<br>Phoenix, Arizona, 85047</p>
      <ul class="contact-list">
        <li>
          <svg viewBox="0 0 24 24" aria-hidden="true"><path fill="#f07c1e" d="M6.6 10.8a15.1 15.1 0 0 0 6.6 6.6l2.2-2.2a1 1 0 0 1 1-.25 11.4 11.4 0 0 0 3.6.57 1 1 0 0 1 1 1V20a1 1 0 0 1-1 1A17 17 0 0 1 3 4a1 1 0 0 1 1-1h3.5a1 1 0 0 1 1 1c0 1.25.2 2.45.57 3.57a1 1 0 0 1-.25 1z"/></svg>
          (602) 517-3094
        </li>
        <li>
          <svg viewBox="0 0 24 24" aria-hidden="true"><path fill="#f07c1e" d="M6 2h9l3 3v4h1a3 3 0 0 1 3 3v8a2 2 0 0 1-2 2H4a2 2 0 0 1-2-2v-8a3 3 0 0 1 3-3h1zm2 2v5h8V6h-2V4zm-2 9v2h2v-2zm4 0v2h2v-2zm4 0v2h2v-2zm-8 4v2h2v-2zm4 0v2h2v-2zm4 0v2h2v-2z"/></svg>
          (602) 768-2145
        </li>
        <li>
          <svg viewBox="0 0 24 24" aria-hidden="true"><circle cx="12" cy="12" r="10" fill="#f07c1e"/><path fill="#111010" d="M7 8c2 0 3 1 3 2s-2 1-2 3 2 2 2 4c-2-.5-4-3-4-5.5 0-1.3.4-2.5 1-3.5zm8-2c1.5.8 3 2.6 3 5-1 0-2-1-3-1s-1 2-2 2-1-2 0-3 2-1 2-3z"/></svg>
          www.SaffronLotusCourt.example
        </li>
      </ul>
    </div>
  </section>

  <section class="card card--front" aria-label="Business card, brand side">
    <p class="brand-name">Saffron<br>Lotus<br>Court</p>
  </section>

</body>
</html>
```